First Aid Training business needs business card design

We would like a double sided business card designed for a first aid training business - Brindlewood First Aid. We provide first aid training and , WHS (work, health and safety) training.

The attached word document contains the key information we would like on each side of the business card.

Final design needs to be delivered in print ready format, along with the original file.

```html
<!DOCTYPE html>
<html lang="en">
<head>
<meta charset="utf-8">
<title>Brindlewood First Aid – Business Card</title>
<link rel="stylesheet" href="https://fonts.googleapis.com/css2?family=Montserrat:wght@400;600;700;800&family=Roboto:ital,wght@0,400;0,500;0,700;1,400;1,500;1,700&display=swap">
<style>
  :root {
    --red: #e8202a;
    --red-deep: #c8141d;
    --grey: #8a8a8a;
    --ink: #1f1f1f;
    --white: #ffffff;
    --card-dark: #222222;
    --page: #d9d9d9;
  }
  * { margin: 0; padding: 0; box-sizing: border-box; }
  html, body { width: 1200px; height: 900px; overflow: hidden; }
  body {
    background: var(--page);
    font-family: "Roboto", Arial, sans-serif;
    position: relative;
  }
  .card {
    position: absolute;
    left: 250px;
    width: 700px;
    height: 400px;
    overflow: hidden;
    box-shadow: 0 6px 18px rgba(0,0,0,0.18);
  }
  .card--front { top: 40px; background: var(--white); }
  .card--back  { top: 460px; background: var(--card-dark); }

  /* Front */
  .front-bands { position: absolute; inset: 0; }
  .brand {
    position: absolute;
    left: 40px;
    top: 150px;
    display: flex;
    align-items: center;
    gap: 12px;
    white-space: nowrap;
  }
  .brand-dot {
    width: 46px; height: 46px;
    border-radius: 50%;
    background: var(--red);
    flex: none;
  }
  .brand-name {
    font-family: "Montserrat", sans-serif;
    font-weight: 700;
    color: var(--ink);
    line-height: 1.1;
  }
  .brand-name .line-main { display: block; font-size: 26px; letter-spacing: 0.3px; }
  .brand-name .line-sub  { display: block; font-size: 12.5px; letter-spacing: 1.5px; }
  .divider {
    position: absolute;
    left: 365px;
    top: 110px;
    width: 1px;
    height: 170px;
    background: var(--grey);
  }
  .person {
    position: absolute;
    left: 392px;
    top: 118px;
    white-space: nowrap;
  }
  .person-name {
    font-family: "Montserrat", sans-serif;
    font-weight: 800;
    font-size: 26px;
    color: var(--red);
    letter-spacing: 1px;
    line-height: 1.15;
  }
  .person-role {
    font-size: 17px;
    color: var(--ink);
    margin-top: 4px;
  }
  .contact-list { list-style: none; margin-top: 20px; }
  .contact-list li {
    display: flex;
    align-items: center;
    gap: 9px;
    font-size: 15px;
    color: var(--ink);
    margin-bottom: 8px;
  }
  .contact-list svg { width: 14px; height: 14px; flex: none; }

  /* Back */
  .back-pattern {
    position: absolute;
    inset: 0;
    background: radial-gradient(ellipse at 85% 30%, #4a4a4a 0%, #2c2c2c 45%, #222 75%);
  }
  .back-copy {
    position: absolute;
    left: 48px;
    bottom: 60px;
    color: var(--white);
    white-space: nowrap;
  }
  .headline {
    font-size: 24px;
    font-weight: 700;
    font-style: italic;
  }
  .headline .accent { color: var(--red); font-weight: 500; }
  .benefits {
    font-size: 16px;
    margin-top: 8px;
  }
  .benefits .bullet { color: var(--red); margin: 0 4px; }
  .services {
    display: flex;
    gap: 34px;
    margin-top: 12px;
    font-size: 20px;
    font-weight: 700;
  }
  .service { display: flex; align-items: center; gap: 9px; }
  .service-mark {
    width: 20px; height: 20px;
    border-radius: 50%;
    border: 2px solid var(--red);
    background: var(--card-dark);
    flex: none;
  }
</style>
</head>
<body>

<section class="card card--front" aria-label="Business card front">
  <svg class="front-bands" viewBox="0 0 700 400" preserveAspectRatio="none" aria-hidden="true">
    <polygon points="0,350 380,390 392,400 0,400" fill="var(--red)"/>
    <polygon points="380,390 700,386 700,400 392,400" fill="var(--grey)"/>
    <polygon points="0,366 380,396 386,400 0,400" fill="var(--red-deep)"/>
  </svg>

  <div class="brand">
    <span class="brand-dot"></span>
    <span class="brand-name">
      <span class="line-main">BRINDLEWOOD</span>
      <span class="line-sub">FIRST AID TRAINING</span>
    </span>
  </div>

  <div class="divider"></div>

  <div class="person">
    <div class="person-name">ALEX MARLOWE</div>
    <div class="person-role">CEO/Founder</div>
    <ul class="contact-list">
      <li>
        <svg viewBox="0 0 16 16"><path d="M3 1.5l3 .5 1 3.5-2 1.2a9 9 0 004.3 4.3l1.2-2 3.5 1 .5 3c-.4 1-1.5 1.6-2.6 1.4C6.6 13.6 2.4 9.4 1.6 4.1 1.4 3 2 1.9 3 1.5z" fill="var(--red)"/></svg>
        0491 570 156
      </li>
      <li>
        <svg viewBox="0 0 16 16"><rect x="1" y="3" width="14" height="10" fill="var(--red)"/><path d="M1 3l7 6 7-6" fill="none" stroke="var(--white)" stroke-width="1.3"/></svg>
        help@brindlewoodfirstaid.com.au
      </li>
      <li>
        <svg viewBox="0 0 16 16"><circle cx="8" cy="8" r="7" fill="var(--red)"/><path d="M1 8h14M8 1c-3 3-3 11 0 14M8 1c3 3 3 11 0 14" fill="none" stroke="var(--white)" stroke-width="1"/></svg>
        www.brindlewoodfirstaid.com.au
      </li>
    </ul>
  </div>
</section>

<section class="card card--back" aria-label="Business card back">
  <div class="back-pattern" role="img" aria-label="Repeating embossed pattern of the company emblem on a dark background"></div>

  <div class="back-copy">
    <p class="headline"><span class="accent">Onsite Training</span> - We can come to you</p>
    <p class="benefits">
      <span class="bullet">•</span>Time efficient
      <span class="bullet">•</span>Cost effective
      <span class="bullet">•</span>Minimise downtime for your team
    </p>
    <div class="services">
      <span class="service"><span class="service-mark"></span>First Aid Training</span>
      <span class="service"><span class="service-mark"></span>WHS Training</span>
    </div>
  </div>
</section>

</body>
</html>
```